Bright Harbor Construction

We are a commercial construction company specializing in steel stud framing, drywall, taping and acoustical ceilings. We would like a company logo (Something that looks great and isnt boring) as we have not been able to come up with one. A modern looking card would definitely suit our personalities best
Updates

We would like to try and avoid using dark colors. I have learned from experience that dark colors are the last to looked at. Thank you

```html
<!DOCTYPE html>
<html lang="en">
<head>
<meta charset="utf-8">
<title>Bright Harbor Construction – Business Card</title>
<link href="https://fonts.googleapis.com/css2?family=Open+Sans:wght@400;600;700&display=swap" rel="stylesheet">
<style>
  :root {
    --red: #b0252d;
    --red-deep: #951f29;
    --charcoal: #444446;
    --slate: #6b6b6e;
    --slate-light: #8c8c90;
    --paper: #f7f7f5;
    --white: #ffffff;
    --stage: #ecebe8;
  }
  * { box-sizing: border-box; margin: 0; padding: 0; }
  html, body { width: 1200px; height: 900px; overflow: hidden; }
  body {
    background: var(--stage);
    font-family: "Open Sans", Arial, sans-serif;
    position: relative;
  }
  .card {
    position: absolute;
    top: 150px;
    width: 350px;
    height: 600px;
    border-radius: 3px;
    overflow: hidden;
    box-shadow: 0 6px 18px rgba(0,0,0,.18);
  }

  /* Back side */
  .card--back {
    left: 200px;
    background: linear-gradient(160deg, var(--slate-light), var(--slate) 60%, #5e5e61);
  }
  .back-pattern {
    position: absolute; left: 0; top: 0; right: 0; height: 400px;
    background: linear-gradient(180deg, #a4a4a8 0%, #8a8a8e 60%, rgba(138,138,142,0) 100%);
  }
  .back-brand {
    position: absolute; left: 30px; bottom: 44px;
    display: flex; align-items: center; gap: 12px;
  }
  .brand-mark { width: 18px; height: 18px; background: var(--red); flex: none; }
  .brand-name {
    color: var(--red);
    font-weight: 700;
    font-size: 28px;
    line-height: 1.1;
    text-transform: uppercase;
  }

  /* Front side */
  .card--front {
    left: 650px;
    background: var(--paper);
    display: flex; flex-direction: column;
  }
  .front-head {
    height: 230px; position: relative; background: var(--white);
  }
  .front-head .brand-name {
    position: absolute; left: 30px; top: 88px; font-size: 20px;
  }
  .skyline {
    position: absolute; right: 22px; top: 50px; width: 110px; height: 130px;
    background: linear-gradient(180deg, #d0d0d0, #6c6c6c);
    border-radius: 2px;
  }
  .band { display: flex; padding: 0 30px; }
  .band--name {
    height: 70px; background: var(--charcoal);
    flex-direction: column; justify-content: center;
  }
  .person-name { color: var(--red); font-size: 19px; font-weight: 600; text-transform: uppercase; line-height: 1.25; }
  .person-role { color: var(--white); font-size: 14px; line-height: 1.3; }
  .band--contact {
    height: 130px;
    background: linear-gradient(180deg, var(--red), var(--red-deep));
    flex-direction: column; justify-content: center;
    color: var(--white); font-size: 14px; line-height: 1.4;
  }
  .contact-line {
    border-bottom: 1px solid rgba(255,255,255,.6);
    padding-bottom: 4px; margin-bottom: 5px; width: 220px;
  }
  .band--specialty { height: 45px; background: var(--white); align-items: center; }
  .specialty-title { color: var(--red); font-size: 20px; font-weight: 700; }
  .band--services {
    height: 95px;
    background: linear-gradient(180deg, var(--charcoal), var(--slate));
    align-items: center;
  }
  .service-list {
    list-style: none; display: grid;
    grid-template-columns: 1fr 1fr; row-gap: 14px; column-gap: 10px;
    width: 100%; color: var(--white); font-size: 13px;
  }
  .service-list li { display: flex; align-items: center; gap: 8px; white-space: nowrap; }
  .service-list li::before { content: ""; width: 7px; height: 7px; border-radius: 50%; background: var(--red); flex: none; }
  .band--more { flex: 1; background: var(--red); color: var(--white); font-size: 13px; align-items: center; }
</style>
</head>
<body>
  <section class="card card--back" aria-label="Card back">
    <div class="back-pattern" role="img" aria-label="Repeating company initials pattern in soft grey"></div>
    <div class="back-brand">
      <span class="brand-mark"></span>
      <span class="brand-name">Bright Harbor<br>Construction</span>
    </div>
  </section>

  <section class="card card--front" aria-label="Card front">
    <header class="front-head">
      <span class="brand-name">Bright Harbor<br>Construction</span>
      <div class="skyline" role="img" aria-label="Grey city skyline illustration"></div>
    </header>
    <div class="band band--name">
      <span class="person-name">Daniel Reyes</span>
      <span class="person-role">President</span>
    </div>
    <div class="band band--contact">
      <span class="contact-line">207.555.0142</span>
      <span class="contact-line">info@brightharborco.com</span>
      <span>48 Millbrook Avenue Suite 3<br>Auburn, ME 04210</span>
    </div>
    <div class="band band--specialty">
      <span class="specialty-title">Specializing In</span>
    </div>
    <div class="band band--services">
      <ul class="service-list">
        <li>Steel Stud Framing</li>
        <li>Acoustical Ceilings</li>
        <li>Insulation</li>
        <li>Drywall &amp; Finishing</li>
      </ul>
    </div>
    <div class="band band--more">And more..</div>
  </section>
</body>
</html>
```